Web Design Project

Hi everyone

Thanks for taking the time to read about this project.

Website needed for Lorel, female singer/songwriter and performer who is launching her debut album this year. She writes and performs folk/pop/soft rock music and plays guitar and piano.

see vidplexa links for examples of Lorel's style:
http://www.vidplexa.com/watch?v=qTbn4Zr8Lp2
http://www.vidplexa.com/watch?v=Kovd7wUheJm

Looking for a classy, modern feel to the website. Cool colours are preferred but open to ideas. It needs it to have CoinDrop set up so items can be purchased from the site. The theme will be continued to Chatterbook and business cards.

Examples include:

http://www.bettyculverdale.com/

http://tessafordyce.com/

http://www.juneqtunes.com/home

Pages and content to be included:

HOME - main picture and general content

BIO - written content about Lorel

NEWS - this will be regularly updated, blog style

GIGS - this will be regularly updated

GALLERY - content will be photos only

SEE AND HEAR - content will be Videos and audios

STORE - this will have a coindrop function for purchase of CD and merchandise

GENEROSITY - this page will be devoted to charity work and updated regularly

CONTACT - information on how to contact Lorel's management

Buttons will need to provide links to Vidplexa, Chirpline, Chatterbook, Snapgrove

I will work closely with the designers in giving feedback as ideas are generated and then provide further content such as photos and videos.

Thanks for considering this project!
Updates

HI everyone thanks for all your submissions so far. Please note the following:

- photos have been uploaded to assist with themes

- background could be a solid colour or texture (e.g. tree trunk texture)

- please use a hand writing font similar to Google font "Give You Glory" - doesn't have to be exactly this but similar

Thank you,

Lorel

Hi again everyone

I apologise but the pixel guild website won't allow me to upload files. I will attempt to correct this as soon as possible. Thanks                                   

18-55 year olds who appreciate this genre of music; gay and lesbian community

Charity

• No flowers or flowery themes

```html
<!DOCTYPE html>
<html lang="en">
<head>
<meta charset="utf-8">
<title>Lorel – Home</title>
<link rel="stylesheet" href="https://fonts.googleapis.com/css2?family=Give+You+Glory&family=Mulish:ital,wght@0,300;0,400;0,600;0,700;1,400;1,700;1,800&display=swap">
<style>
  :root {
    --page: #ffffff;
    --frame-line: #7a7a7a;
    --label: #666666;
    --wood-dark: #2b211b;
    --wood-mid: #4a3a30;
    --wood-light: #5d4b3f;
    --teal-bg: #6aa9a8;
    --teal-bg-2: #5f9fa0;
    --card: #d3e5e2;
    --share-box: rgba(24, 92, 104, 0.85);
    --nav-line: #3f8fa3;
    --nav-text: #8fd3e3;
    --nav-active: #2e7d90;
    --ink: #2d2d2d;
    --show-blue: #1e5f8e;
    --row: #24a592;
    --row-edge: #d8eeea;
    --date: #d3e27c;
    --buy: #a78c5a;
    --buy-text: #f4ecd8;
    --badge: #d7e8ec;
    --badge-text: #1c3a6a;
    --player: #1b1b1b;
    --player-red: #d71920;
    --video-frame: #d6e4e2;
    --brand: #d8d2c8;
    --white: #ffffff;
  }
  * { box-sizing: border-box; margin: 0; padding: 0; }
  html, body { width: 1200px; height: 1000px; overflow: hidden; background: var(--page); }
  body { position: relative; font-family: "Mulish", sans-serif; }

  .frame { position: absolute; left: 87px; top: 116px; width: 1024px; height: 768px; border: 1px solid var(--frame-line); }
  .site {
    position: absolute; left: 117px; top: 116px; width: 966px; height: 768px; overflow: hidden;
    box-shadow: 0 0 14px rgba(0,0,0,.45);
  }
  .wood { position: absolute; inset: 0; background: linear-gradient(90deg, var(--wood-dark), var(--wood-mid) 20%, var(--wood-light) 45%, var(--wood-mid) 70%, var(--wood-dark)); }

  .brand { position: absolute; left: 238px; top: 28px; font-family: "Mulish", sans-serif; font-weight: 300; font-size: 84px; line-height: 1; letter-spacing: 2px; color: var(--brand); }

  .share { position: absolute; left: 638px; top: 0; width: 300px; height: 50px; background: var(--share-box); display: flex; align-items: center; padding: 0 12px; gap: 8px; }
  .share-links { display: grid; grid-template-columns: auto auto; gap: 2px 10px; }
  .share-links a { color: var(--white); font-size: 11px; font-weight: 700; text-decoration: none; }
  .share-label { font-family: "Give You Glory", cursive; color: #cfe7ee; font-size: 34px; line-height: 1; margin-left: auto; }

  .nav { position: absolute; left: 0; top: 126px; width: 966px; height: 32px; border-top: 2px solid var(--nav-line); border-bottom: 2px solid var(--nav-line); background: rgba(20,60,70,.25); }
  .nav a { position: absolute; top: 3px; font-size: 18px; letter-spacing: 1px; color: var(--nav-text); text-decoration: none; }
  .nav a.active { left: 1px; top: 0; height: 28px; width: 97px; background: var(--nav-active); color: var(--white); font-weight: 700; padding: 3px 0 0 21px; }

  .content { position: absolute; left: 0; top: 172px; width: 966px; height: 576px; background: linear-gradient(180deg, var(--teal-bg), var(--teal-bg-2)); }

  .card { position: absolute; top: 10px; width: 294px; height: 188px; background: var(--card); border-radius: 24px; }
  .card p { position: absolute; font-size: 10.5px; line-height: 13.3px; color: var(--ink); text-align: justify; letter-spacing: .3px; }
  .photo { position: absolute; }
  .card-singer { left: 42px; }
  .card-singer .photo { left: 6px; top: -4px; width: 130px; height: 186px; transform: rotate(-1.5deg); border: 3px solid var(--white); background: linear-gradient(160deg, #5a3fb0, #3a3450 50%, #6b5d72); }
  .card-singer p { left: 139px; top: 17px; width: 145px; }
  .card-piano { left: 349px; }
  .card-piano .quote { left: 17px; top: 10px; width: 104px; font-style: italic; font-weight: 400; font-size: 13px; line-height: 17px; letter-spacing: .5px; }
  .card-piano .photo { left: 131px; top: 9px; width: 149px; height: 130px; border: 3px solid var(--white); background: linear-gradient(160deg, #111, #3a3a3a 45%, #cfc9c0 70%, #a8a39c); }
  .show-note { position: absolute; left: 76px; top: 140px; font-family: "Give You Glory", cursive; font-size: 30px; color: var(--show-blue); white-space: nowrap; }
  .card-guitar { left: 656px; }
  .card-guitar .photo { left: 2px; top: -6px; width: 94px; height: 194px; border-radius: 40px 40px 44px 44px; background: linear-gradient(180deg, #b9741e, #4a2a1e 18%, #4a2a1e); }
  .card-guitar p { left: 109px; top: 17px; width: 168px; }

  .heading { position: absolute; font-style: italic; font-weight: 400; color: var(--white); letter-spacing: 1px; line-height: 1; }
  .see-hear-title { left: 48px; top: 218px; font-size: 35px; }
  .video-frame { position: absolute; left: 48px; top: 248px; width: 441px; height: 264px; background: var(--video-frame); }
  .video { position: absolute; left: 41px; top: 258px; width: 442px; height: 245px; background: linear-gradient(160deg, #0d0d0d, #2a1e18 45%, #5a4030 65%, #1a1410); }
  .player { position: absolute; left: 41px; top: 503px; width: 442px; height: 24px; background: var(--player); }
  .video-caption { position: absolute; left: 34px; top: 534px; font-style: italic; font-weight: 800; font-size: 24px; color: var(--white); white-space: nowrap; }

  .pay-badge { position: absolute; left: 828px; top: 217px; width: 122px; height: 42px; background: var(--badge); clip-path: polygon(10% 0, 100% 0, 92% 100%, 0 100%); display: flex; align-items: center; justify-content: center; font-weight: 700; font-size: 17px; color: var(--badge-text); text-decoration: none; }

  .schedule-title { left: 561px; top: 276px; font-size: 35px; }
  .show { position: absolute; left: 561px; width: 389px; height: 82px; background: var(--row); border: 2px solid var(--row-edge); }
  .show .date { position: absolute; left: 13px; bottom: 14px; color: var(--date); font-weight: 300; white-space: nowrap; line-height: 1; }
  .show .month { font-size: 25px; letter-spacing: -1px; }
  .show .day { font-size: 50px; letter-spacing: -2px; }
  .show .city { position: absolute; left: 146px; top: 45px; font-style: italic; font-weight: 700; font-size: 13px; letter-spacing: 1px; color: var(--white); }
  .show .buy { position: absolute; left: 301px; top: 20px; width: 65px; height: 40px; background: var(--buy); color: var(--buy-text); font-weight: 300; font-size: 31px; text-align: center; line-height: 40px; text-decoration: none; }

  .size-label { position: absolute; left: 87px; top: 905px; width: 1024px; height: 36px; }
  .size-label .rule { position: absolute; top: 18px; height: 1px; width: 399px; background: var(--frame-line); }
  .size-label .text { position: absolute; left: 0; width: 100%; top: 0; text-align: center; font-size: 26px; color: var(--label); }
</style>
</head>
<body>
  <div class="frame"></div>

  <div class="site">
    <div class="wood" role="img" aria-label="Dark weathered wooden plank texture background"></div>

    <header>
      <div class="brand">Lorel</div>
      <div class="share">
        <nav class="share-links">
          <a href="#">Chatterbook</a>
          <a href="#">Chirpline</a>
          <a href="#">Snapgrove</a>
          <a href="#">Vidplexa</a>
        </nav>
        <span class="share-label">share</span>
      </div>
      <nav class="nav">
        <a class="active" href="#">Home</a>
        <a href="#" style="left:121px">Bio</a>
        <a href="#" style="left:194px">News</a>
        <a href="#" style="left:288px">Gigs</a>
        <a href="#" style="left:372px">Gallery</a>
        <a href="#" style="left:481px">See &amp; Hear</a>
        <a href="#" style="left:626px">Store</a>
        <a href="#" style="left:719px">Generosity</a>
        <a href="#" style="left:863px">Contact</a>
      </nav>
    </header>

    <main class="content">
      <section class="card card-singer">
        <div class="photo" role="img" aria-label="Photo of Lorel singing at a microphone under purple stage light"></div>
        <p>"Lorem ipsum dolor sit amet, consectetur adip-isicing elit, sed do eius-mod tempor incididunt ut labore et dolore magna aliqua. Ut enim ad minim veniam!</p>
      </section>

      <section class="card card-piano">
        <p class="quote">"Lorem ipsum dolor sit amet, Con-sectetur adip-isicing elit, sed do!</p>
        <div class="photo" role="img" aria-label="Photo of hands playing piano keys"></div>
        <div class="show-note">june 25th show</div>
      </section>

      <section class="card card-guitar">
        <div class="photo" role="img" aria-label="Illustration of an acoustic guitar"></div>
        <p>"Lorem ipsum dolor sit amet, Consectetur adipisicing elit, sed do eiusmod tempor inci-didunt ut labore et dolore magna aliqua. Ut enim ad minim veniam! consectetur adipisicing elit, sed do eius-mod tempor incididunt ut labore et dolore magna aliqua. Ut enim ad minim veniam!</p>
      </section>

      <h2 class="heading see-hear-title">See &amp; Hear</h2>
      <div class="video-frame"></div>
      <div class="video" role="img" aria-label="Video still of Lorel performing with an acoustic guitar"></div>
      <div class="player">
        <svg width="442" height="24" viewBox="0 0 442 24">
          <rect x="0" y="0" width="442" height="5" fill="#444"/>
          <rect x="0" y="0" width="44" height="5" fill="var(--player-red)"/>
          <circle cx="45" cy="3" r="4" fill="#ddd"/>
          <polygon points="12,11 12,21 20,16" fill="#bbb"/>
          <rect x="38" y="13" width="4" height="6" fill="#bbb"/>
          <polygon points="42,13 48,10 48,22 42,19" fill="#bbb"/>
          <text x="60" y="20" font-size="8" fill="#ccc" font-family="Mulish, sans-serif">0:16 / 2:49</text>
          <circle cx="348" cy="16" r="4" fill="none" stroke="#bbb" stroke-width="2"/>
          <circle cx="369" cy="16" r="3" fill="#bbb"/>
          <rect x="384" y="12" width="10" height="7" fill="none" stroke="#bbb" stroke-width="2"/>
          <rect x="404" y="12" width="12" height="7" fill="none" stroke="#bbb" stroke-width="1.5"/>
          <path d="M424 11h3M424 11v3M437 11h-3M437 11v3M424 21h3M424 21v-3M437 21h-3M437 21v-3" stroke="#bbb" stroke-width="1.5" fill="none"/>
        </svg>
      </div>
      <p class="video-caption">watch Lorel's latest Vidplexa video</p>

      <a class="pay-badge" href="#">CoinDrop</a>

      <h2 class="heading schedule-title">Show Schedule</h2>
      <article class="show" style="top:306px">
        <div class="date"><span class="month">JUN</span><span class="day">25</span></div>
        <div class="city">Boston, MA</div>
        <a class="buy" href="#">BUY</a>
      </article>
      <article class="show" style="top:393px">
        <div class="date"><span class="month">JUL</span><span class="day">3</span></div>
        <div class="city">Los Angeles, CA</div>
        <a class="buy" href="#">BUY</a>
      </article>
      <article class="show" style="top:481px">
        <div class="date"><span class="month">JUL</span><span class="day">12</span></div>
        <div class="city">Brooklyn, NYC</div>
        <a class="buy" href="#">BUY</a>
      </article>
    </main>
  </div>

  <div class="size-label">
    <span class="rule" style="left:0"></span>
    <span class="text">1024 x 768</span>
    <span class="rule" style="right:0"></span>
  </div>
</body>
</html>
```